Marrow Lane needs new business cards

Business card design for Marrow Lane (Australia's leading award winning beeswax candle company)
Designed with logo colours Black and Gold
and logo included on the front card (maybe water marked on back of card?)

Marrow Lane Pty Ltd
Greta Pellowe
CEO & Lead Maker
greta@marrowlaneco.com.au
0418672243

and our tag line "Warm your evenings, Brighten every room " somewhere

The back of the card should read

Specialists in Weddings, Bonbonniere , Corporate and Special Occasion's

Target Market(s)

women 15-65

Industry/Entity Type

Business

Contact Information for Business Card

Marrow Lane Pty Ltd
Greta Pellowe
CEO & Lead Maker
0418672243

Colors
ffc214
000000

Requirements
Must have
• as above
• I love the look of Tessa Vardy Paris
Nice to have
• look luxurious
• Beautiful font
• Border scroll
• refer to website
• marrowlaneco.com.au
Should not have
• any other colours

```html
<!DOCTYPE html>
<html lang="en">
<head>
<meta charset="utf-8">
<title>Marrow Lane – Business Card</title>
<link rel="stylesheet" href="https://fonts.googleapis.com/css2?family=Tinos&display=swap">
<style>
  :root {
    --card-bg: #121410;
    --gold: #c9a22c;
    --gold-soft: rgba(201, 162, 44, 0.55);
    --gold-fade: rgba(201, 162, 44, 0);
  }
  html, body {
    margin: 0;
    padding: 0;
    width: 720px;
    height: 1200px;
    overflow: hidden;
    background: var(--card-bg);
  }
  .card {
    position: relative;
    width: 720px;
    height: 1200px;
    background: var(--card-bg);
    font-family: "Tinos", "Times New Roman", serif;
    color: var(--gold);
    text-align: center;
  }
  .ornament {
    position: absolute;
    left: 240px;
    width: 240px;
    height: 72px;
    border-radius: 50%;
    background: radial-gradient(ellipse at center, var(--gold-soft) 0%, var(--gold-fade) 70%);
  }
  .ornament--top { top: 72px; }
  .ornament--bottom { top: 1048px; }

  .brand-name {
    position: absolute;
    top: 355px;
    left: 0;
    width: 100%;
    margin: 0;
    font-size: 60px;
    font-weight: 400;
    letter-spacing: 4px;
    line-height: 1;
  }
  .rule {
    position: absolute;
    left: 36px;
    width: 648px;
    height: 16px;
  }
  .rule--upper { top: 516px; }
  .rule--lower { top: 648px; }

  .text {
    position: absolute;
    left: 0;
    width: 100%;
    margin: 0;
    font-weight: 400;
    line-height: 1;
    white-space: nowrap;
  }
  .company  { top: 574px; font-size: 34px; }
  .person   { top: 708px; font-size: 31px; }
  .role     { top: 757px; font-size: 19px; }
  .email    { top: 833px; font-size: 26px; }
  .phone    { top: 887px; font-size: 26px; }
  .tagline  { top: 967px; font-size: 29px; }
</style>
</head>
<body>
  <main class="card">
    <div class="ornament ornament--top" role="img" aria-label="Gold filigree scroll ornament"></div>

    <h1 class="brand-name">Marrow Lane</h1>

    <svg class="rule rule--upper" viewBox="0 0 648 16" aria-hidden="true">
      <line x1="8" y1="8" x2="640" y2="8" stroke="#c9a22c" stroke-width="2"/>
      <circle cx="8" cy="8" r="7" fill="#c9a22c"/>
      <circle cx="640" cy="8" r="7" fill="#c9a22c"/>
    </svg>

    <p class="text company">Marrow Lane Pty Ltd</p>

    <svg class="rule rule--lower" viewBox="0 0 648 16" aria-hidden="true">
      <line x1="8" y1="8" x2="640" y2="8" stroke="#c9a22c" stroke-width="2"/>
      <circle cx="8" cy="8" r="7" fill="#c9a22c"/>
      <circle cx="640" cy="8" r="7" fill="#c9a22c"/>
    </svg>

    <p class="text person">Greta Pellowe</p>
    <p class="text role">CEO &amp; Lead Maker</p>

    <p class="text email">greta@marrowlaneco.com.au</p>
    <p class="text phone">0418672243</p>

    <p class="text tagline">"Warm your evenings, Brighten every room "</p>

    <div class="ornament ornament--bottom" role="img" aria-label="Gold filigree scroll ornament"></div>
  </main>
</body>
</html>
```